Computer consultant business card

Brimlo Software is a newly started computer consulting company. It's a small one-man company that provides mostly Velunix applications but also websites in collaboration with designers. I'm running this company on the side of full time university studies.

I want the final design to be clean and memorable. Be creative! :)

Some inspiration:
http://www.tavelpix.net/design/73519
http://www.tavelpix.net/design/2739566/business-card-design-by-quillbop
http://www.tavelpix.net/design/804613/business-card-design-by-lorvena-brukwaldsen

See attachment for my company logo.
Updates

I would like to thank everyone for submitting! I'll need a couple of days to review and ultimately select a design.

Target Market(s)

Non-technical entrepreneurs and small companies.

Industry/Entity Type

University

Requirements
Must have
• My company logo.
In any way, both colors from my logo.
First- and last name, e-mail and phone number.
Double-sided design.
Nice to have
• Something creative with the symbol in my logo

```html
<!DOCTYPE html>
<html lang="en">
<head>
<meta charset="utf-8">
<title>Brimlo Software – Business Card</title>
<link rel="stylesheet" href="https://fonts.googleapis.com/css2?family=Open+Sans:wght@400;600;700&display=swap">
<style>
  :root {
    --page-bg: #ecebe8;
    --card-dark: #3a3939;
    --card-dark-deep: #2e2d2d;
    --card-light: #ffffff;
    --brand-blue: #4672c0;
    --ink-white: #ffffff;
    --ink-dark: #2b2b2b;
    --faint-grey: #e4e4ea;
    --faint-dark: #444343;
  }
  * { box-sizing: border-box; margin: 0; padding: 0; }
  html, body {
    width: 1200px;
    height: 1016px;
    overflow: hidden;
    background: var(--page-bg);
    font-family: "Open Sans", Arial, sans-serif;
  }
  .canvas {
    position: relative;
    width: 1200px;
    height: 1016px;
  }
  .card {
    position: absolute;
    left: 300px;
    width: 600px;
    height: 343px;
    border-radius: 22px;
    overflow: hidden;
    box-shadow: 0 6px 18px rgba(0,0,0,0.18);
  }
  .card--front {
    top: 110px;
    background: radial-gradient(circle at 55% 50%, #424141 0%, var(--card-dark) 45%, var(--card-dark-deep) 100%);
  }
  .card--back {
    top: 563px;
    background: var(--card-dark);
  }
  .faint-circle {
    position: absolute;
    border-radius: 50%;
  }
  .card--front .faint-circle {
    width: 300px; height: 300px;
    left: 165px; top: 22px;
    background: var(--faint-dark);
  }
  .brand {
    position: absolute;
    display: flex;
    align-items: center;
    gap: 18px;
  }
  .brand__dot {
    width: 58px; height: 58px;
    border-radius: 50%;
    background: var(--brand-blue);
  }
  .brand__name {
    font-weight: 700;
    line-height: 1;
    letter-spacing: 1px;
  }
  .card--front .brand { left: 150px; top: 130px; }
  .card--front .brand__name { font-size: 76px; color: var(--ink-white); }

  .back-art {
    position: absolute;
    inset: 0;
    width: 600px;
    height: 343px;
  }
  .card--back .brand { left: 30px; top: 66px; gap: 12px; }
  .card--back .brand__dot { width: 36px; height: 36px; }
  .card--back .brand__name { font-size: 46px; color: var(--ink-dark); }

  .identity {
    position: absolute;
    right: 36px;
    top: 30px;
    text-align: right;
  }
  .identity__name {
    font-size: 22px;
    font-weight: 600;
    letter-spacing: 1px;
    color: var(--brand-blue);
  }
  .identity__title {
    font-size: 15px;
    font-weight: 700;
    color: var(--ink-white);
    margin-top: -2px;
  }
  .contact {
    position: absolute;
    right: 30px;
    top: 196px;
    text-align: right;
    color: var(--ink-white);
    font-size: 16px;
    line-height: 1.5;
    letter-spacing: 0.5px;
  }
  .contact__row { display: flex; align-items: center; justify-content: flex-end; gap: 8px; }
  .contact__icon { width: 12px; height: 14px; flex: none; }
</style>
</head>
<body>
<main class="canvas">

  <section class="card card--front" aria-label="Card front">
    <div class="faint-circle" aria-hidden="true"></div>
    <div class="brand">
      <span class="brand__dot" aria-hidden="true"></span>
      <span class="brand__name">Brimlo</span>
    </div>
  </section>

  <section class="card card--back" aria-label="Card back">
    <svg class="back-art" viewBox="0 0 600 343" aria-hidden="true">
      <path d="M0 0 L250 0 C325 40 352 200 296 343 L0 343 Z" fill="var(--card-light)"/>
      <path d="M250 0 L266 0 C342 40 368 200 311 343 L296 343 C352 200 325 40 250 0 Z" fill="var(--brand-blue)"/>
      <circle cx="165" cy="265" r="100" fill="var(--faint-grey)"/>
    </svg>

    <div class="brand">
      <span class="brand__dot" aria-hidden="true"></span>
      <span class="brand__name">Brimlo</span>
    </div>

    <div class="identity">
      <p class="identity__name">YOUR NAME</p>
      <p class="identity__title">Job Title</p>
    </div>

    <div class="contact">
      <p class="contact__row">000-000-000
        <svg class="contact__icon" viewBox="0 0 12 14" aria-hidden="true"><rect x="2" y="0.5" width="8" height="13" rx="1.5" fill="none" stroke="#fff" stroke-width="1.2"/><rect x="5" y="11" width="2" height="1" fill="#fff"/></svg>
      </p>
      <p class="contact__row">name@domainname.com
        <svg class="contact__icon" viewBox="0 0 12 14" aria-hidden="true"><rect x="0.5" y="3" width="11" height="8" fill="#fff"/><path d="M0.5 3 L6 7.5 L11.5 3" fill="none" stroke="#3a3939" stroke-width="1"/></svg>
      </p>
    </div>
  </section>

</main>
</body>
</html>
```